New Business Cards for Velmora

About Velmora:
At Velmora, we're more than just a company—we're a force for positive change in the staffing industry. Our brand is our heartbeat, and we need a designer who can translate that into every design element.

The Project:
We're revamping our business cards and need your artistic flair to make them stand out. Here's what we're looking for:

- Incorporate our existing brand elements (logo, colours, fonts) into the design.
- Craft a design that's sleek, professional, and memorable.
- Provide options for different layouts and finishes.
- Collaborate closely with our team to ensure the final product exceeds expectations.

Please note: For general text, we use Avenir. The brand guidelines are slightly out of date and don't have correct imaging. Colours are correct though.

```html
<!DOCTYPE html>
<html lang="en">
<head>
<meta charset="utf-8">
<title>Velmora — Business Cards</title>
<link href="https://fonts.googleapis.com/css2?family=Nunito+Sans:wght@400;600&display=swap" rel="stylesheet">
<style>
  :root {
    --plum: #5e2d79;
    --magenta: #e0197d;
    --ink: #4a4a4a;
    --rule: #6b6b6b;
    --paper: #ffffff;
    --stage: #ece9e5;
    --back-start: #5d3277;
    --back-end: #93306f;
    --icon-green: #3bb54a;
  }
  * { margin: 0; padding: 0; box-sizing: border-box; }
  html, body {
    width: 900px; height: 1200px; overflow: hidden;
    background: var(--stage);
    font-family: "Nunito Sans", "Avenir", sans-serif;
  }
  .canvas { position: relative; width: 900px; height: 1200px; }

  .card {
    position: absolute; left: 87px; width: 735px; height: 430px;
    border-radius: 28px;
    box-shadow: 0 4px 14px rgba(0,0,0,0.18);
  }
  .card--front { top: 136px; background: var(--paper); }
  .card--back {
    top: 632px;
    background: linear-gradient(100deg, var(--back-start) 0%, var(--back-end) 100%);
  }

  /* brand name set in the text font, with one plain circle beside it */
  .brand { position: absolute; display: flex; align-items: center; }
  .brand__mark { flex: none; border-radius: 50%; background: var(--magenta); }
  .brand__text { text-align: center; }
  .brand__name { font-weight: 600; line-height: 1; letter-spacing: 0; }
  .brand__tagline { font-weight: 400; }

  .card--front .brand { left: 72px; top: 153px; height: 128px; gap: 16px; }
  .card--front .brand__mark { width: 62px; height: 62px; }
  .card--front .brand__name { font-size: 50px; color: var(--plum); }
  .card--front .brand__tagline { font-size: 14px; color: var(--plum); margin-top: 8px; }

  .divider {
    position: absolute; left: 413px; top: 127px;
    width: 1.5px; height: 177px; background: var(--rule);
  }

  .contact { position: absolute; left: 446px; top: 136px; color: var(--ink); }
  .contact__name { font-size: 24px; font-weight: 600; letter-spacing: 0.3px; line-height: 1; }
  .contact__first { color: var(--plum); }
  .contact__last { color: var(--magenta); }
  .contact__role { font-size: 16px; margin-top: 10px; letter-spacing: 0.4px; }
  .contact__list { list-style: none; margin-top: 24px; }
  .contact__item {
    display: flex; align-items: center; gap: 9px;
    font-size: 16.5px; letter-spacing: 0.4px; height: 29.5px;
  }
  .contact__icon { width: 16px; height: 16px; flex: none; }

  .card--back .brand { left: 0; width: 735px; top: 142px; height: 146px; justify-content: center; gap: 20px; }
  .card--back .brand__mark { width: 72px; height: 72px; }
  .card--back .brand__name { font-size: 60px; color: var(--paper); }
  .card--back .brand__tagline { font-size: 16px; color: var(--paper); margin-top: 10px; }

  .web {
    position: absolute; left: 0; width: 735px; top: 381px;
    text-align: center; font-size: 15px; color: var(--paper); letter-spacing: 0.3px;
  }
  .web__domain { color: var(--magenta); }
</style>
</head>
<body>
<main class="canvas">

  <section class="card card--front" aria-label="Business card front">
    <div class="brand">
      <span class="brand__mark" aria-hidden="true"></span>
      <div class="brand__text">
        <div class="brand__name">Velmora</div>
        <p class="brand__tagline">people first, always</p>
      </div>
    </div>

    <div class="divider"></div>

    <div class="contact">
      <h1 class="contact__name"><span class="contact__first">DANIEL</span> <span class="contact__last">WHITFORD</span></h1>
      <p class="contact__role">Founder and CEO</p>
      <ul class="contact__list">
        <li class="contact__item">
          <svg class="contact__icon" viewBox="0 0 16 16" aria-hidden="true">
            <circle cx="8" cy="8" r="8" fill="var(--icon-green)"/>
            <path d="M5.4 4.2c.3-.2.7-.2.9.1l.8 1.2c.2.3.1.6-.1.8l-.5.4c.4.9 1.1 1.6 2 2l.4-.5c.2-.2.6-.3.8-.1l1.2.8c.3.2.3.6.1.9l-.5.6c-.4.4-1 .5-1.5.3C7.2 10 6 8.8 5.3 7c-.2-.5-.1-1.1.3-1.5z" fill="#fff"/>
          </svg>
          + 1 (555) 010 2468
        </li>
        <li class="contact__item">
          <svg class="contact__icon" viewBox="0 0 16 16" aria-hidden="true">
            <rect x="1" y="3" width="14" height="10" rx="1" fill="var(--plum)"/>
            <path d="M1.5 4l6.5 5 6.5-5" fill="none" stroke="#fff" stroke-width="1.2"/>
          </svg>
          whitford@velmora.com
        </li>
        <li class="contact__item">
          <svg class="contact__icon" viewBox="0 0 16 16" aria-hidden="true" fill="none" stroke="var(--magenta)" stroke-width="1.2">
            <circle cx="8" cy="8" r="6.5"/>
            <ellipse cx="8" cy="8" rx="2.8" ry="6.5"/>
            <path d="M1.5 8h13M2.5 5h11M2.5 11h11"/>
          </svg>
          www.velmora.com
        </li>
      </ul>
    </div>
  </section>

  <section class="card card--back" aria-label="Business card back">
    <div class="brand">
      <span class="brand__mark" aria-hidden="true"></span>
      <div class="brand__text">
        <div class="brand__name">Velmora</div>
        <p class="brand__tagline">people first, always</p>
      </div>
    </div>
    <p class="web">www.<span class="web__domain">velmora</span>.com</p>
  </section>

</main>
</body>
</html>
```